Home Inspection Postcard Design

Home inspection. Attached is my old postcard. I would like the card to have the same verbage on it - front and back. but I would like the house graphic and the colors to be blues. The only changes to the information is the website address is www.brightoakhps.com. THe PO Box is now 381 rather than 647, and I wanted to add my email address which is brightoakhps@quillmail.net. I would like to keep the $25 off box but add "or a 10% military discount, which ever is greater" or something like that .If you could mock something up for me I would really appreciate it. I would also like a glossy finish on the cards

Home Inspection

```html
<!DOCTYPE html>
<html lang="en">
<head>
<meta charset="utf-8">
<title>Bright Oak Home Inspection Postcard</title>
<link href="https://fonts.googleapis.com/css2?family=Arimo:ital,wght@0,400;0,700;1,400;1,700&family=Roboto+Condensed:wght@300;400&display=swap" rel="stylesheet">
<style>
  :root{
    --royal:#2b2f95;
    --royal-deep:#22267f;
    --ink:#1a1a1a;
    --lavender:#8f8fcf;
    --sky:#c9cdf0;
    --yellow:#f2d21b;
    --white:#ffffff;
    --page:#f1f1f1;
  }
  *{box-sizing:border-box;margin:0;padding:0}
  html,body{width:1200px;height:837px;overflow:hidden;background:var(--page)}
  body{position:relative;font-family:"Arimo",Arial,sans-serif}
  .postcard{position:absolute;top:197px;width:570px;height:442px;overflow:hidden;box-shadow:4px 5px 10px rgba(0,0,0,.35)}
  .postcard--front{left:22px}
  .postcard--back{left:608px;background:var(--white)}

  /* front */
  .street-photo{position:absolute;inset:0;background:
    linear-gradient(180deg,#f4f5fb 0%,#dcdff3 30%,#b4b6e2 60%,#6c6cb8 85%,#3d3f95 100%)}
  .brand{position:absolute;text-align:center;color:var(--royal)}
  .brand__name{font-size:40px;font-weight:400;line-height:1}
  .brand__sub{font-size:13px;letter-spacing:.3px;margin-top:4px}
  .postcard--front .brand{left:150px;top:42px;width:260px}
  .intro{position:absolute;left:20px;top:119px;width:530px;height:159px;background:rgba(255,255,255,.8);
    padding:5px 6px;font-style:italic;font-size:12.6px;line-height:16.4px;color:var(--ink);text-align:justify}
  .intro p+p{margin-top:16px}
  .contact{position:absolute;left:30px;top:299px;width:320px;text-align:center;color:var(--yellow);
    font-size:14.5px;line-height:19.5px;text-shadow:0 0 3px rgba(0,0,0,.55)}
  .contact strong{font-weight:700;font-style:italic}
  .motto{position:absolute;left:34px;top:374px;width:340px;text-align:center;color:var(--white);font-style:italic;
    text-shadow:0 0 3px rgba(0,0,0,.5)}
  .motto__quote{font-size:21px;letter-spacing:1px}
  .motto__creds{font-size:14.5px;margin-left:70px}
  .offer{position:absolute;left:399px;top:290px;width:159px;height:135px;background:var(--royal);color:var(--white);
    text-align:center;padding-top:8px}
  .offer__headline{font-size:15.5px;font-weight:700;color:#8fb0ff}
  .offer__detail{font-size:12.5px;font-weight:700;line-height:15.5px}
  .offer__rule{width:132px;height:1px;background:var(--white);margin:6px auto 8px}
  .offer__alt{font-size:12.5px;font-weight:700;font-style:italic;line-height:15.5px}
  .offer__note{font-size:8.5px;margin-top:4px}

  /* back */
  .postcard--back .brand{left:18px;top:26px;width:190px;text-align:left}
  .postcard--back .brand__name{font-size:34px}
  .postcard--back .brand__sub{font-size:10.5px}
  .return-address{position:absolute;left:230px;top:40px;font-size:11.5px;color:var(--royal)}
  .web-band{position:absolute;left:0;top:105px;width:570px;height:53px;background:var(--royal);color:var(--white);
    font-size:21px;font-weight:700;letter-spacing:5.6px;line-height:53px;padding-left:26px}
  .stamp{position:absolute;left:430px;top:15px;width:124px;height:124px}
  .about{position:absolute;left:22px;top:167px;width:250px;font-family:"Roboto Condensed",Arial,sans-serif;
    font-weight:300;font-size:10.4px;line-height:13.6px;color:var(--royal);text-align:justify}
  .address-lines{position:absolute;left:294px;top:205px;width:246px;height:130px}
</style>
</head>
<body>

<section class="postcard postcard--front">
  <div class="street-photo" role="img" aria-label="Blue-toned photo of a cobblestone lane lined with white clapboard houses"></div>
  <div class="brand">
    <div class="brand__name">Bright Oak</div>
    <div class="brand__sub">Home Inspection Services LLC.</div>
  </div>
  <div class="intro">
    <p>Enjoy the comfort of peace-of-mind before buying your new home. Our trained, professionals inspect the property and immediately present you with a detailed yet clear report. They will answer any questions you may have.</p>
    <p>Join our experienced inspectors in their tour of the property. They will acquaint you with its strengths and weaknesses. You will feel confident in their judgement and thoroughness. Many realtors, sellers, home buyers, mortgage companies and relocation companies have used our comprehensive report and services to their satisfaction.</p>
  </div>
  <div class="contact">
    Call <strong>912.555.0148</strong> or<br>
    email <strong>brightoakhps@quillmail.net</strong><br>
    to schedule your appointment today!
  </div>
  <div class="motto">
    <div class="motto__quote">“we leave no stone unturned”</div>
    <div class="motto__creds">Licensed, Ceritified, &amp; Insured</div>
  </div>
  <div class="offer">
    <div class="offer__headline">Get $25 off</div>
    <div class="offer__detail">our services with<br>this postcard!</div>
    <div class="offer__rule"></div>
    <div class="offer__alt">or a 10%<br>military discount</div>
    <div class="offer__note">(whichever is greater)</div>
  </div>
</section>

<section class="postcard postcard--back">
  <div class="brand">
    <div class="brand__name">Bright Oak</div>
    <div class="brand__sub">Home Inspection Services LLC.</div>
  </div>
  <div class="return-address">P.O. Box 381 - Marlow, GA 31399</div>
  <div class="web-band">www.brightoakhps.com</div>
  <svg class="stamp" viewBox="0 0 124 124" aria-hidden="true">
    <rect x="1" y="1" width="122" height="122" fill="#fff" stroke="#1a1a1a" stroke-width="1.5"/>
    <line x1="1" y1="1" x2="123" y2="123" stroke="#1a1a1a" stroke-width="1"/>
    <line x1="123" y1="1" x2="1" y2="123" stroke="#1a1a1a" stroke-width="1"/>
  </svg>
  <p class="about">The purchase of a home or commercial building is one of the largest single investments you will ever make. You should know what to expect in terms of needed &amp; possible repairs &amp; maintenance. A fresh coat of paint could be hiding serious problems. Stains on the ceiling may indicate a chronic roof leak or may be the result of a single incident. The inspector reviews these and other clues then presents a professional opinion as to the condition of the property to help you avoid unpleasant surprises afterwards. Of course, an inspection may also point out the positive aspects of a building, as well as the type of maintenance needed to keep it in proper shape. After the inspection you will have a much clearer understanding of the property and be able to make your purchasing decision confidently.</p>
  <svg class="address-lines" viewBox="0 0 246 130" aria-hidden="true">
    <g stroke="#1a1a1a" stroke-width="1">
      <line x1="0" y1="6" x2="246" y2="6"/>
      <line x1="0" y1="35" x2="246" y2="35"/>
      <line x1="0" y1="64" x2="246" y2="64"/>
      <line x1="0" y1="93" x2="246" y2="93"/>
      <line x1="0" y1="122" x2="246" y2="122"/>
    </g>
  </svg>
</section>

</body>
</html>
```